"Brightwall Sound Living Residences" need a busines Card Design got Builder

We need a business card design for a company based in Milford, Michigancalled Brightwall Sound Living Residences - has been recognized as a premier custom home builder. Distinguished by outstanding craftmanship and timeless beauty. Our custom home can be found in the most prestigious communities in Michigan. The homes are built with ICF (insulated concrete homes) which is green, allergy free, fire free, mold free and quitter. Our slogan "building one dream at a Time" and also we are ICF distributor for the state of Michigan

Target Market(s)

Anyone who is making over $100,000 a year and who wants to have totally custom built home. Ages from 29 up to 60 years old

Industry/Entity Type

Concrete

Contact Information for Business Card

we want to use - green, black, gray or blue colors - we want to look different with our business cards, because we built homes only with ICF, green, healthier and highly energy efficient homes.

Requirements
Must have
• I have logo that I attached and we have been using the logo (the only green home)
Nice to have
• should look quality business card,

Files

```html
<!DOCTYPE html>
<html lang="en">
<head>
<meta charset="utf-8">
<title>Brightwall Sound Living Residences – Business Card</title>
<link href="https://fonts.googleapis.com/css2?family=Open+Sans:wght@400;600;700&display=swap" rel="stylesheet">
<style>
  :root {
    --page-bg: #e6e7ea;
    --navy: #263f8f;
    --navy-deep: #1f3478;
    --royal: #2f56a8;
    --sky: #4d86cf;
    --paper: #ffffff;
    --paper-shade: #eceef1;
    --brand-grey: #8a8d93;
    --ink: #2a2a2e;
    --name-blue: #3f7cc6;
  }
  * { box-sizing: border-box; margin: 0; padding: 0; }
  html, body {
    width: 1200px; height: 900px; overflow: hidden;
    background: var(--page-bg);
    font-family: "Open Sans", Arial, sans-serif;
  }
  .stage {
    width: 1200px; height: 900px;
    display: flex; align-items: center; justify-content: center;
  }
  .card {
    position: relative;
    width: 1050px; height: 600px;
    border-radius: 56px;
    overflow: hidden;
    background: var(--paper);
    box-shadow: 0 14px 40px rgba(0,0,0,0.18);
  }
  .card-shapes { position: absolute; inset: 0; }
  .address-block {
    position: absolute; left: 70px; top: 122px;
    color: var(--paper);
    font-size: 27px; line-height: 1.35; font-weight: 400;
  }
  .contact-list {
    position: absolute; left: 74px; top: 402px;
    list-style: none;
    color: var(--paper);
    font-size: 16px; line-height: 1;
  }
  .contact-list li {
    display: flex; align-items: center; gap: 10px;
    height: 26px;
  }
  .contact-list svg { width: 15px; height: 15px; flex: none; }
  .brand {
    position: absolute; left: 560px; top: 70px; width: 420px;
    display: flex; flex-direction: column; align-items: center;
  }
  .brand-dot {
    width: 110px; height: 110px; border-radius: 50%;
    background: var(--navy);
    margin-bottom: 22px;
  }
  .brand-name {
    color: var(--brand-grey);
    font-size: 27px; font-weight: 400;
    letter-spacing: 1px; line-height: 1.1;
    text-transform: uppercase; text-align: center;
  }
  .person {
    position: absolute; right: 62px; top: 360px;
    text-align: right;
  }
  .person-name {
    color: var(--name-blue);
    font-size: 30px; font-weight: 700; letter-spacing: 1px;
    text-transform: uppercase;
  }
  .person-title {
    color: var(--ink);
    font-size: 19px; font-weight: 400; margin-top: 4px;
  }
</style>
</head>
<body>
<main class="stage">
  <section class="card">
    <svg class="card-shapes" viewBox="0 0 1050 600" preserveAspectRatio="none" aria-hidden="true">
      <defs>
        <radialGradient id="panelGlow" cx="0.28" cy="0.4" r="0.7">
          <stop offset="0" stop-color="var(--royal)"/>
          <stop offset="1" stop-color="var(--navy-deep)"/>
        </radialGradient>
        <radialGradient id="paperGlow" cx="0.55" cy="0.35" r="0.7">
          <stop offset="0" stop-color="var(--paper)"/>
          <stop offset="1" stop-color="var(--paper-shade)"/>
        </radialGradient>
      </defs>
      <rect width="1050" height="600" fill="var(--paper)"/>
      <rect width="760" height="600" fill="url(#panelGlow)"/>
      <circle class="swoosh-accent" cx="880" cy="210" r="470" fill="var(--sky)"/>
      <circle class="swoosh-gap" cx="900" cy="190" r="462" fill="var(--paper)"/>
      <circle class="paper-disc" cx="915" cy="170" r="455" fill="url(#paperGlow)"/>
    </svg>

    <p class="address-block">041.12th floor,Orchard<br>Crest Road MFD</p>

    <ul class="contact-list">
      <li>
        <svg viewBox="0 0 16 16"><path fill="currentColor" d="M3.6 1.2l2.2 2.9-1.3 1.5c.9 2 2.6 3.7 4.6 4.6l1.5-1.3 2.9 2.2-1.4 2.6C6.8 13.5 2.5 9.2 1 3.1z"/></svg>
        <span>014 552 0183</span>
      </li>
      <li>
        <svg viewBox="0 0 16 16"><rect x="1" y="3" width="14" height="10" rx="1" fill="currentColor"/><path d="M1.5 3.8L8 9l6.5-5.2" fill="none" stroke="var(--navy)" stroke-width="1.3"/></svg>
        <span>hello@brightwallsound.com</span>
      </li>
      <li>
        <svg viewBox="0 0 16 16" fill="none" stroke="currentColor" stroke-width="1.4"><circle cx="8" cy="8" r="6.5"/><ellipse cx="8" cy="8" rx="2.8" ry="6.5"/><path d="M1.5 8h13M2.5 4.8h11M2.5 11.2h11"/></svg>
        <span>www.brightwallsound.com</span>
      </li>
      <li>
        <svg viewBox="0 0 16 16"><path fill="currentColor" d="M8 0.8a5 5 0 0 0-5 5c0 3.8 5 9.4 5 9.4s5-5.6 5-9.4a5 5 0 0 0-5-5zm0 7a2 2 0 1 1 0-4 2 2 0 0 1 0 4z"/></svg>
        <span>041.12th floor,Orchard Crest Road MFD</span>
      </li>
    </ul>

    <div class="brand">
      <span class="brand-dot" aria-hidden="true"></span>
      <p class="brand-name">Brightwall Sound<br>Living Residences</p>
    </div>

    <div class="person">
      <p class="person-name">Daniel Whitford</p>
      <p class="person-title">Managing Director</p>
    </div>
  </section>
</main>
</body>
</html>
```